Rising Paths Web Design

I am starting a new company that will provide LIFE COACHING services - I have tried to design a website, but it's too complicated. Right now, it's just me - I'm the only person that will provide services through the website - I have used artmarket to purchase a logo (see below). I want to be able to update the website myself, but need a template - basic design. Because I am not technologically savvy enough to explain in words - I basically want to have a website that will provide basic information about my services (coaching), a page about me and my background, hopefully scheduling possibilities, and testimonials — also a page for writing/blogs. I bought a website through NetHarbor - so when I have a template, I guess I”d use that - but maybe I’ll need to work with a designer to actually get it up on the internet. I have a head shot that I’ll upload, too.
Target Market(s)
Clients from the independent (private school) world - teachers, administrators
Number of Pages Required
4 page
Look and feel
Each slider illustrates characteristics of the customer's brand and the style your logo design should communicate.

```html
<!DOCTYPE html>
<html lang="en">
<head>
<meta charset="utf-8">
<title>Rising Paths Coaching</title>
<link href="https://fonts.googleapis.com/css2?family=Fredoka:wght@500;600&family=Mulish:wght@300;400;600;700&display=swap" rel="stylesheet">
<style>
:root{
  --teal:#0a9b8c;
  --teal-dark:#0b4a48;
  --ink:#0c4e4b;
  --mint:#c5eee7;
  --white:#ffffff;
  --text:#2f5f5c;
}
*{margin:0;padding:0;box-sizing:border-box}
html,body{width:1200px;height:1200px;overflow:hidden;background:var(--white)}
body{font-family:"Mulish",sans-serif;color:var(--text)}
.stage{position:relative;width:1932px;height:1932px;transform:scale(0.6211);transform-origin:0 0}
.a{position:absolute}
.heading{font-family:"Fredoka",sans-serif;font-weight:600;color:var(--ink)}
.label{font-size:5px;letter-spacing:.1px;text-transform:uppercase;color:var(--ink)}
.small{font-size:5.3px;line-height:8.5px;color:var(--text)}
.btn{background:var(--teal);color:var(--white);display:flex;align-items:center;justify-content:center;text-decoration:none}
/* header */
.brand{left:778px;top:6px;width:52px;height:42px}
.brand-ring{width:38px;height:38px;border:1px solid var(--teal);border-radius:50%;position:absolute;left:2px;top:2px}
.brand-name{font-weight:600;font-size:6.2px;color:var(--ink);position:absolute;left:3px;top:19px;white-space:nowrap}
.nav{top:23px;font-size:5.5px;font-weight:700;color:var(--teal)}
.nav-home{text-decoration:underline}
.book{left:1119px;top:14px;width:68px;height:20px;font-size:5.5px;font-weight:700}
/* hero */
.hero-photo{left:748px;top:55px;width:235px;height:275px;border-top-right-radius:8px;
  background:
    radial-gradient(ellipse 70px 85px at 118px 140px,rgba(244,214,170,.9) 0%,rgba(230,196,150,.55) 45%,rgba(230,196,150,0) 100%),
    radial-gradient(ellipse 90px 60px at 118px 230px,rgba(245,240,230,.9) 0%,rgba(245,240,230,0) 100%),
    radial-gradient(ellipse 160px 120px at 40px 200px,rgba(60,200,180,.55) 0%,rgba(60,200,180,0) 100%),
    linear-gradient(140deg,#0a5f58 0%,#139a8c 45%,#0d7268 100%)}
.hero-band{left:748px;top:280px;width:235px;height:40px;background:rgba(16,160,145,.88);padding:5px 0 0 38px;color:var(--white);font-weight:300}
.hero-band .name{font-size:10px;line-height:12px}
.hero-band .role{font-size:13.5px;line-height:17px}
.hero-band b{font-weight:700}
.hero-title{left:1011px;top:103px;font-size:16px;line-height:19px;width:158px}
.hero-text{left:1012px;top:159px;width:172px;font-size:5.8px;line-height:9.7px}
.hero-btn{left:1011px;top:226px;width:102px;height:23px;font-size:6.8px}
.cert{left:1012px;top:271px;font-size:5.5px;font-weight:700;color:var(--teal)}
.badge{top:291px;width:24px;height:24px;border-radius:3px}
/* advantages */
.advantages{left:748px;top:330px;width:469px;height:345px;background:var(--mint)}
.adv-title{left:787px;top:402px;font-size:15px;line-height:20.3px;width:150px}
.feature-icon{fill:none;stroke:var(--ink);stroke-width:1.2;stroke-linecap:round;stroke-linejoin:round}
.feature-title{font-family:"Fredoka",sans-serif;font-weight:500;font-size:6.5px;color:var(--ink)}
/* blog */
.center{left:748px;width:469px;text-align:center}
.card-img{top:825px;width:124px;height:159px;
  background:
    radial-gradient(ellipse 22px 40px at 62px 75px,rgba(104,118,72,.75) 0%,rgba(104,118,72,0) 100%),
    radial-gradient(ellipse 30px 70px at 112px 60px,rgba(120,80,50,.6) 0%,rgba(120,80,50,0) 100%),
    radial-gradient(ellipse 70px 30px at 60px 140px,rgba(92,64,44,.8) 0%,rgba(92,64,44,0) 100%),
    linear-gradient(180deg,#f2f3ef 0%,#e3e4dc 45%,#b9ab95 75%,#6e5844 100%)}
.card-title{top:992px;font-size:8px}
.card-date{top:1005px;font-size:5px;color:var(--ink)}
.card-text{top:1018px;width:100px}
/* promo */
.promo-left{left:748px;top:1090px;width:300px;height:261px;
  background:
    radial-gradient(ellipse 80px 120px at 120px 120px,rgba(200,240,232,.45) 0%,rgba(200,240,232,0) 100%),
    linear-gradient(180deg,#94dccf 0%,#7ccfc2 100%)}
.promo-right{left:1048px;top:1090px;width:169px;height:261px;
  background:
    radial-gradient(ellipse 45px 55px at 118px 55px,rgba(120,80,50,.85) 0%,rgba(120,80,50,0) 100%),
    radial-gradient(ellipse 55px 130px at 122px 190px,rgba(122,78,52,.95) 0%,rgba(122,78,52,0) 100%),
    linear-gradient(120deg,#2a2f2e 0%,#3a3e3c 50%,#5a4234 100%)}
.watch{left:768px;top:1174px;font-size:10px;font-weight:700;color:var(--ink)}
.promo-card{left:904px;top:1141px;width:221px;height:159px;background:var(--white)}
/* testimonials */
.avatar{left:950px;top:1489px;width:56px;height:56px;border-radius:50%;
  background:
    radial-gradient(ellipse 12px 15px at 28px 24px,#c79a7e 0%,rgba(199,154,126,0) 100%),
    radial-gradient(ellipse 20px 12px at 28px 52px,#2c3a48 0%,rgba(44,58,72,0) 100%),
    linear-gradient(160deg,#e7ddd0,#b9a590)}
.quote{left:829px;top:1563px;width:306px;text-align:center;font-size:5.8px;line-height:9.3px;font-weight:600;color:var(--ink)}
.dot{top:1667px;width:6px;height:6px;border-radius:50%;background:#5e9c98}
/* footer */
.footer{left:748px;top:1717px;width:469px;height:183px;background:var(--mint)}
.foot-brand-ring{left:802px;top:1742px;width:60px;height:62px;border:1px solid var(--teal);border-radius:50%}
.foot-brand{left:806px;top:1770px;font-size:9px;font-weight:600;color:var(--ink);white-space:nowrap}
.foot-head{font-size:7.5px}
.foot-text{font-size:5.5px;line-height:8.5px;color:var(--ink)}
.bottom-bar{left:748px;top:1900px;width:469px;height:32px;background:var(--teal-dark);color:#cfe9e6;font-size:5.5px;display:flex;align-items:center;justify-content:center}
</style>
</head>
<body>
<div class="stage">

  <!-- header -->
  <div class="a brand"><span class="brand-ring"></span><span class="brand-name">RISING PATHS</span></div>
  <span class="a nav nav-home" style="left:884px">Home</span>
  <span class="a nav" style="left:916px">About</span>
  <span class="a nav" style="left:948px">Services</span>
  <span class="a nav" style="left:987px">Contact Us</span>
  <span class="a nav" style="left:1054px">(+1)555 0142</span>
  <a class="a btn book">Book a Session</a>

  <!-- hero -->
  <div class="a hero-photo" role="img" aria-label="Smiling head shot of the coach on a teal wave background"></div>
  <div class="a hero-band"><div class="name">Name Comes Here</div><div class="role">SUPER <b>LIFE COACHING</b></div></div>
  <p class="a label" style="left:1012px;top:90px">Start your journey with us!</p>
  <h1 class="a heading hero-title">Welcome to Rising Paths</h1>
  <p class="a hero-text">In publishing and graphic design, Lorem ipsum is a placeholder text commonly used to demonstrate the visual form of a document or a typeface without relying on meaningful content.</p>
  <a class="a btn hero-btn">Start your journey Now!</a>
  <p class="a cert">Certified Professional</p>
  <div class="a badge" style="left:1012px;background:#1f5679" role="img" aria-label="Certification badge"></div>
  <div class="a badge" style="left:1057px;border-radius:50%;border:2px solid #27a3c9" role="img" aria-label="Certification badge"></div>
  <div class="a badge" style="left:1099px;background:#2a5a86" role="img" aria-label="Certification badge"></div>

  <!-- advantages -->
  <section class="a advantages"></section>
  <p class="a label" style="left:787px;top:391px">What do we offer to people</p>
  <h2 class="a heading adv-title">Advantages you get after, joining our Life Coaching services!</h2>
  <p class="a small" style="left:965px;top:390px;width:170px">In publishing and graphic design, Lorem ipsum is a placeholder text commonly used to demonstrate the visual form of a document or a typeface</p>

  <svg class="a feature-icon" style="left:968px;top:435px" width="32" height="28" viewBox="0 0 32 28" aria-label="Coaching icon">
    <rect x="1" y="2" width="30" height="19" rx="1.5"/><path d="M5 6h10M5 10h7M5 14h9"/><path d="M19 15l4-6 4 4"/><path d="M12 26l4-5 4 5"/>
  </svg>
  <p class="a feature-title" style="left:965px;top:472px">Coaching</p>
  <p class="a small" style="left:965px;top:483px;width:68px">In publishing and graphic design, Lorem ipsum is a placeholder text</p>

  <svg class="a feature-icon" style="left:1101px;top:435px" width="26" height="28" viewBox="0 0 26 28" aria-label="Super hero icon">
    <path d="M13 2l3 7h7l-5.5 4.5 2 7.5L13 16.5 6.5 21l2-7.5L3 9h7z"/><path d="M6 26h14"/>
  </svg>
  <p class="a feature-title" style="left:1091px;top:472px">You be a Super Hero</p>
  <p class="a small" style="left:1091px;top:483px;width:68px">In publishing and graphic design, Lorem ipsum is a placeholder text</p>

  <svg class="a feature-icon" style="left:966px;top:531px" width="34" height="32" viewBox="0 0 34 32" aria-label="Self confidence icon">
    <rect x="2" y="2" width="11" height="8" rx="1"/><path d="M5 10l-1 3 4-3"/><rect x="19" y="1" width="12" height="9" rx="1"/><path d="M22 5.5l2 2 4-4"/><path d="M6 30V20h22v10"/><path d="M11 24h12"/><path d="M30 24v4M28 26h4"/>
  </svg>
  <p class="a feature-title" style="left:962px;top:571px">Self Confidence</p>
  <p class="a small" style="left:962px;top:586px;width:68px">In publishing and graphic design, Lorem ipsum is a placeholder text</p>

  <svg class="a feature-icon" style="left:1103px;top:530px" width="32" height="32" viewBox="0 0 32 32" aria-label="Renew your energy icon">
    <circle cx="17" cy="14" r="7"/><path d="M17 10v8M15 12h3.5a1.5 1.5 0 010 3H15.5a1.5 1.5 0 000 3H19"/><path d="M9 4a13 13 0 0116-1"/><path d="M25 3l1 3-3 0"/><path d="M2 26c4-3 8-3 12 0h8c3 0 6-2 8-4"/>
  </svg>
  <p class="a feature-title" style="left:1091px;top:571px">Renew your energy</p>
  <p class="a small" style="left:1091px;top:586px;width:68px">In publishing and graphic design, Lorem ipsum is a placeholder text</p>

  <!-- blog -->
  <p class="a center" style="top:729px;font-size:5px;color:var(--ink)">Blog space</p>
  <h2 class="a heading center" style="top:747px;font-size:15px;padding-left:14px">My latest blog</h2>

  <div class="a card-img" style="left:789px" role="img" aria-label="Photo of a coach presenting to a group in an office"></div>
  <h3 class="a heading card-title" style="left:789px">My blog post1</h3>
  <p class="a card-date" style="left:790px">25 Jun 2022</p>
  <p class="a small card-text" style="left:789px">In publishing and graphic design, Lorem ipsum is a placeholder text</p>

  <div class="a card-img" style="left:920px" role="img" aria-label="Photo of a coach presenting to a group in an office"></div>
  <h3 class="a heading card-title" style="left:920px">My blog post2</h3>
  <p class="a card-date" style="left:921px">25 Jun 2022</p>
  <p class="a small card-text" style="left:920px">In publishing and graphic design, Lorem ipsum is a placeholder text</p>

  <div class="a card-img" style="left:1052px" role="img" aria-label="Photo of a coach presenting to a group in an office"></div>
  <h3 class="a heading card-title" style="left:1051px">My blog post3</h3>
  <p class="a card-date" style="left:1052px">25 Jun 2022</p>
  <p class="a small card-text" style="left:1051px">In publishing and graphic design, Lorem ipsum is a placeholder text</p>

  <!-- promo -->
  <div class="a promo-left" role="img" aria-label="Faded photo of a classroom under a teal overlay"></div>
  <div class="a promo-right" role="img" aria-label="Photo of a teacher with folded arms in front of a chalkboard"></div>
  <p class="a watch">WATCH OUR VIDEO</p>
  <p class="a small" style="left:770px;top:1194px;width:104px;line-height:9px">Introduction Video on our <b>Life Coaching</b> understand our methods of coaching.</p>
  <svg class="a" style="left:794px;top:1237px" width="36" height="36" viewBox="0 0 36 36" aria-label="Play video">
    <circle cx="18" cy="18" r="16.5" fill="none" stroke="#3a6e6a" stroke-width="1.3"/>
    <path d="M13 12 L25 18 L13 24 Z" fill="#3a6e6a"/>
  </svg>
  <div class="a promo-card"></div>
  <p class="a label" style="left:927px;top:1161px">Building the future, restoring the past</p>
  <h2 class="a heading" style="left:926px;top:1172px;width:185px;font-size:15px;line-height:19px">Reserve your seat and start your journey!</h2>
  <p class="a small" style="left:927px;top:1219px;width:160px">In publishing and graphic design, Lorem ipsum is a placeholder textipsum is a placeholder text</p>
  <a class="a btn" style="left:927px;top:1245px;width:73px;height:20px;font-size:6px">Call us now</a>

  <!-- testimonials -->
  <p class="a center" style="top:1403px;font-size:5px;color:var(--ink);padding-right:10px">What others tells about my coaching</p>
  <h2 class="a heading center" style="top:1420px;font-size:14px">Client Testimonials</h2>
  <div class="a avatar" role="img" aria-label="Client portrait photo"></div>
  <p class="a quote">In publishing and graphic design, Lorem ipsum is a placeholder text commonly used to demonstrate the visual form of a document or a typeface without relying on meaningful content. Lorem ipsum may be used as a placeholder before final copy is available.</p>
  <p class="a center" style="top:1607px;font-size:5.8px;line-height:9.5px;color:var(--ink);padding-right:18px"><b>Daniel Harper,</b><br>Teacher, ABC Schools</p>
  <span class="a dot" style="left:960px;background:var(--teal-dark)"></span>
  <span class="a dot" style="left:970px"></span>
  <span class="a dot" style="left:980px"></span>

  <!-- footer -->
  <footer class="a footer"></footer>
  <span class="a foot-brand-ring"></span>
  <span class="a foot-brand">RISING PATHS</span>
  <h4 class="a heading foot-head" style="left:958px;top:1754px">ADDRESS LINE</h4>
  <p class="a foot-text" style="left:958px;top:1764px">Address comes here,<br>Address comes here.</p>
  <h4 class="a heading foot-head" style="left:1045px;top:1754px">Email Details</h4>
  <p class="a foot-text" style="left:1045px;top:1764px">info@domainname.com</p>
  <h4 class="a heading foot-head" style="left:1045px;top:1791px">Contact Details</h4>
  <p class="a foot-text" style="left:1045px;top:1801px">Address comes here,<br>Address comes here.</p>
  <div class="a bottom-bar">© 2022 All Rights reserved with yourdomainname.com</div>

</div>
</body>
</html>
```